Retail Bacon Package Design

We need a printed topfilm design for a variety of our retail range of bacon. We currently have a range of retail sausages where we get a topfilm printed with an image to seal our packs. The brief is to create a design for our retail bacon range which is in line with our current range of retail sausages as well as our shipper. I have attached a few examples of current packs (Harlow Bacon) as well as from a competitor (Pim) to show what we are trying to achieve. We will need approx 4 different types to start with, such as

Maple Bacon (Dry cured, Cold Smoked, Short Cut)
Maple Bacon (Dry Cured, Cold Smoked, Streaky)
Short Cut Bacon (Triple Smoked)
Streaky Bacon (Triple Smoked)

```html
<!DOCTYPE html>
<html lang="en">
<head>
<meta charset="utf-8">
<title>Retail Bacon Package Design</title>
<link href="https://fonts.googleapis.com/css2?family=Oswald:wght@500;700&display=swap" rel="stylesheet">
<style>
  :root {
    --board: #3a3a3a;
    --title: #fff6b0;
    --peach: #fdd3a8;
    --walnut: #4f2603;
    --cream: #fdf9d8;
    --black: #000000;
    --yellow: #fff200;
    --red: #ff3300;
    --brand-red: #e0283c;
    --brand-cream: #fbe9c8;
  }
  * { box-sizing: border-box; margin: 0; padding: 0; }
  html, body { width: 1200px; height: 1200px; overflow: hidden; }
  body {
    background: var(--board);
    font-family: "Oswald", sans-serif;
    position: relative;
  }
  .pack {
    position: absolute;
    top: 312px;
    width: 342px;
    height: 482px;
    overflow: hidden;
    box-shadow: 14px 14px 18px rgba(0,0,0,0.75);
  }
  .pack--short-cut { left: 52px; background: var(--peach); }
  .pack--streaky-dark { left: 429px; background: var(--walnut); }
  .pack--streaky-light { left: 806px; background: var(--cream); }

  .art { position: absolute; }

  .brand {
    position: absolute;
    left: 150px;
    top: 58px;
    width: 180px;
    display: flex;
    align-items: center;
    justify-content: center;
    gap: 8px;
    font-weight: 700;
    font-size: 22px;
    letter-spacing: 1px;
    color: var(--brand-red);
  }
  .pack--streaky-dark .brand { color: var(--brand-cream); }
  .brand__dot {
    width: 16px; height: 16px; border-radius: 50%;
    background: var(--brand-red);
  }

  .label {
    position: absolute;
    left: 28px;
    top: 241px;
    width: 143px;
    height: 241px;
    background: var(--black);
    text-align: center;
  }
  .pack--streaky-light .label { background: var(--red); }
  .label__name {
    margin-top: 20px;
    font-weight: 700;
    font-size: 48px;
    line-height: 46px;
    color: var(--yellow);
    text-transform: uppercase;
  }
  .label__spec {
    margin-top: 18px;
    font-weight: 500;
    font-size: 17px;
    line-height: 21.5px;
    color: var(--red);
  }
  .pack--streaky-light .label__spec { color: var(--black); }
  .label__weight {
    display: inline-block;
    margin-top: 20px;
    padding: 0 4px;
    background: var(--yellow);
    color: var(--black);
    font-weight: 700;
    font-size: 16px;
    line-height: 20px;
  }
  .pack--streaky-light .label__weight { color: var(--red); }

  .board-title {
    position: absolute;
    left: 0;
    top: 924px;
    width: 1200px;
    text-align: center;
    font-weight: 700;
    font-size: 84px;
    line-height: 100px;
    color: var(--title);
  }
</style>
</head>
<body>

  <section class="pack pack--short-cut">
    <div class="art" role="img" aria-label="Illustration of orange flames and white smoke"
         style="left:0;top:0;width:160px;height:230px;background:linear-gradient(160deg,#ff5a1a,#fdd3a8 80%);"></div>
    <div class="art" role="img" aria-label="Illustration of rising smoke, tomatoes and a chilli"
         style="left:170px;top:190px;width:172px;height:140px;background:linear-gradient(200deg,#ffffff,#fdd3a8 75%);opacity:.8;"></div>
    <div class="art" role="img" aria-label="Illustration of a kettle grill with steak, zucchini and capsicum"
         style="left:180px;top:330px;width:162px;height:152px;border-radius:80px 0 0 0;background:linear-gradient(135deg,#c9e83a,#d42d1f 45%,#1d1d1d 80%);"></div>
    <div class="brand"><span class="brand__dot"></span>ALPINE LARDER</div>
    <div class="label">
      <p class="label__name">Maple<br>Bacon</p>
      <p class="label__spec">Dry cured<br>Cold Smoked<br>Short Cut</p>
      <p class="label__weight">160g</p>
    </div>
  </section>

  <section class="pack pack--streaky-dark">
    <div class="art" role="img" aria-label="Illustration of a plate with grilled sausages, fish and lemon"
         style="left:0;top:0;width:135px;height:150px;border-radius:0 0 70px 0;background:linear-gradient(135deg,#e84a2a,#f4efe6 70%);"></div>
    <div class="art" role="img" aria-label="Illustration of an onion half"
         style="left:278px;top:200px;width:45px;height:40px;border-radius:50%;background:linear-gradient(135deg,#f6e2d4,#e46a3a);"></div>
    <div class="art" role="img" aria-label="Illustration of two meat and vegetable skewers"
         style="left:185px;top:250px;width:157px;height:232px;background:linear-gradient(160deg,#4f2603,#e8342a 35%,#ffc21a 75%,#4f2603);"></div>
    <div class="brand"><span class="brand__dot"></span>ALPINE LARDER</div>
    <div class="label">
      <p class="label__name">Maple<br>Bacon</p>
      <p class="label__spec">Dry Cured<br>Cold Smoked<br>Streaky</p>
      <p class="label__weight">160g</p>
    </div>
  </section>

  <section class="pack pack--streaky-light">
    <div class="art" role="img" aria-label="Illustration of orange flames with pale yellow smoke"
         style="left:0;top:0;width:150px;height:220px;background:linear-gradient(160deg,#ff5a1a,#fdf9d8 80%);"></div>
    <div class="art" role="img" aria-label="Illustration of a steak and a sausage on forks"
         style="left:205px;top:290px;width:137px;height:192px;background:linear-gradient(170deg,#b3231c,#d9402a 40%,#b9b9b9 75%,#fdf9d8);"></div>
    <div class="brand"><span class="brand__dot"></span>ALPINE LARDER</div>
    <div class="label">
      <p class="label__name">Maple<br>Bacon</p>
      <p class="label__spec">Dry Cured<br>Cold Smoked<br>Streaky</p>
      <p class="label__weight">160g</p>
    </div>
  </section>

  <h1 class="board-title">Retail Bacon Package Design</h1>

</body>
</html>
```